Promotional Flyer/Email Design - Cabling services for Broadcast and Audio Visual

We need a promotional flyer/email design to help launch our company, Velcor Lane. We provide cabling services for Broadcast Television and Audio Visual systems. Recent projects include major television events such as the Harrowmere Racquet Classic and Audio Visual/Entertainment systems for wealthy clients in their homes and on-board super yachts.

The flyer will be printed as single sided A5 and also be sent out in the body of a promotional email. It should feature the company logo along with a complementary colour scheme. It should have a clean finish with images that show the type of work we do (cabling and equipment installation) or the setting for these systems (tv studio, super yacht, cinema room, meeting room with projector etc.)

Services we offer are:

Broadcast/AV system design
On-site installation
Rack building
Pre-fabricated cable looms
Fibre optic installation

About the company:

Velcor Lane provide cabling services for Broadcast Television and Audio Visual systems. With over 15 years experience working in these industries we can help with every aspect of design, project managment, installation and maintenance. Our projects range from fibre optic cabling at major sports events to installing and commisioning bespoke control systems on some of the worlds largest super yachts.

Contact details:

To get a quote or discuss your project contact us now
Telephone: TBC
Email: info@velcor-lane.com
Website: www.velcor-lane.com
Address: TBC

Other information:

The company is based in London, UK. Our projects often take place in other countries with work taking place accross Europe and beyond.

We have a London based workshop for rack building and cable pre-fabrication.

Our website is www.velcor-lane.com

Images:

Images attached can be editted for use on the flyer or have ideas taken from them. Only the company logo is required to feature on the final design.

Target Market(s)

Business to business

Industry/Entity Type

It Company

Font styles to use
Sans Serif

Requirements
Must have
• Company logo
• List of services
• Contact details
Nice to have
• Image of cabling, home cinema room, super yacht, luxury home, outside broadcast truck, fibre optic equipment or cabling.

```html
<!DOCTYPE html>
<html lang="en">
<head>
<meta charset="utf-8">
<title>Velcor Lane – Broadcast &amp; AV System Installation</title>
<link href="https://fonts.googleapis.com/css2?family=Open+Sans:wght@400;600;700;800&family=Quicksand:wght@400;500;600&display=swap" rel="stylesheet">
<style>
:root{
  --red:#e0203c;
  --blue:#2a5fae;
  --blue-deep:#235aa6;
  --dark:#2c2c2e;
  --ink:#333;
  --rule:#cfd3d8;
  --paper:#f3f4f6;
}
*{margin:0;padding:0;box-sizing:border-box}
html,body{width:998px;height:1200px;overflow:hidden;background:#fff}
.flyer{position:relative;width:998px;height:1200px;overflow:hidden;background:linear-gradient(180deg,#fbfbfc 0%,var(--paper) 100%);font-family:"Open Sans",sans-serif;color:var(--ink)}

/* hero imagery */
.hero{position:absolute;left:0;top:0;width:998px;height:470px}
.hero-main{position:absolute;inset:0;background:linear-gradient(180deg,#dde3ea 0%,#b9c3cf 35%,#e9edf2 62%,#cfd9e6 100%)}
.thumb{position:absolute;border:4px solid var(--blue);box-shadow:0 2px 6px rgba(0,0,0,.25)}
.thumb-rack{left:20px;top:24px;width:200px;height:128px;background:linear-gradient(180deg,#e9ecef,#b7bcc2)}
.thumb-lounge{left:34px;top:170px;width:200px;height:128px;background:linear-gradient(180deg,#8a7a66,#c9b9a0)}
.thumb-cable{left:48px;top:318px;width:200px;height:128px;background:linear-gradient(180deg,#d9aa74,#c28f58)}
.hero-rule{position:absolute;left:0;top:470px;width:998px;height:10px;background:var(--blue)}
.hero-rule::after{content:"";position:absolute;left:0;top:10px;width:998px;height:5px;background:var(--dark)}

/* left column */
.headline{position:absolute;left:58px;top:508px;line-height:1}
.headline .l1{font-weight:800;font-size:56px;color:var(--red);letter-spacing:-.5px}
.headline .l2{margin-top:12px;font-size:40px;color:var(--blue)}
.headline .l2 b{font-weight:800;letter-spacing:-.5px}
.headline .l2 span{font-weight:400}

.section-title{font-size:27px;line-height:1.3;color:var(--blue);font-weight:400}
.section-title em{font-style:normal;color:var(--red);font-weight:700}
.section-title i{font-family:"Quicksand",sans-serif;font-style:normal;font-weight:500}

.services{position:absolute;left:68px;top:640px;width:410px}
.service-list{list-style:none;margin-top:12px}
.service-list li{display:flex;align-items:center;gap:18px;height:54px;border-bottom:1px solid var(--rule);font-family:"Quicksand",sans-serif;font-weight:600;font-size:23px;color:#6b6b6b}
.service-list li:last-child{border-bottom:none}
.service-list svg{width:30px;height:30px;flex:none}

/* right column */
.about{position:absolute;left:530px;top:500px;width:420px}
.other{position:absolute;left:545px;top:790px;width:415px}
.about p,.other p{margin-top:16px;font-size:16px;line-height:1.45;color:var(--ink);text-align:justify}
.other p+p{margin-top:16px}

/* footer */
.footer-shape{position:absolute;left:0;top:990px;width:998px;height:210px}
.brand{position:absolute;left:70px;top:1066px;display:flex;align-items:center;gap:16px}
.brand-dot{width:38px;height:38px;background:var(--red)}
.brand-name{font-weight:700;font-size:44px;line-height:1;color:var(--dark);letter-spacing:-.5px}
.contact{position:absolute;top:1062px;color:#fff;font-size:18px;line-height:34px;list-style:none}
.contact li{display:flex;align-items:center;gap:12px}
.contact svg{width:17px;height:17px;flex:none}
.contact-a{left:425px}
.contact-b{left:708px}
.contact .phone{font-weight:700;font-size:20px}
</style>
</head>
<body>
<main class="flyer">
  <section class="hero">
    <div class="hero-main" role="img" aria-label="Photo of a large white TV studio hall with a gallery level and colour-bar backdrop reflected in a glossy floor"></div>
    <div class="thumb thumb-rack" role="img" aria-label="Photo of a wall-mounted equipment panel with cabling"></div>
    <div class="thumb thumb-lounge" role="img" aria-label="Photo of a luxury lounge with a wall-mounted television"></div>
    <div class="thumb thumb-cable" role="img" aria-label="Photo of a coiled fibre optic cable with connectors"></div>
  </section>
  <div class="hero-rule"></div>

  <h1 class="headline">
    <div class="l1">BROADCAST &amp;</div>
    <div class="l2"><b>AV SYSTEM</b> <span>Installation</span></div>
  </h1>

  <section class="services">
    <h2 class="section-title"><em>OUR</em> SERVICES:</h2>
    <ul class="service-list">
      <li><svg viewBox="0 0 32 32" fill="none" stroke="#aaa" stroke-width="2.4"><circle cx="16" cy="13" r="3"/><path d="M10 19a8 8 0 1 1 12 0M6 23a13 13 0 1 1 20 0M16 16v14"/></svg>Broadcast/AV system design</li>
      <li><svg viewBox="0 0 32 32" fill="none" stroke="#aaa" stroke-width="3"><circle cx="16" cy="16" r="5"/><path d="M16 3v6M16 23v6M3 16h6M23 16h6M7 7l4 4M21 21l4 4M25 7l-4 4M11 21l-4 4"/></svg>On-site installation</li>
      <li><svg viewBox="0 0 32 32" fill="none" stroke="#aaa" stroke-width="2.2"><path d="M3 16 16 4l13 12M7 13v16h18V13"/><path d="M13 29v-8h6v8"/></svg>Rack building</li>
      <li><svg viewBox="0 0 32 32" fill="none" stroke="#aaa" stroke-width="2.2"><rect x="4" y="8" width="10" height="12" rx="2"/><path d="M7 8V3M11 8V3M9 20v5a4 4 0 0 0 8 0v-6a4 4 0 0 1 8 0v10"/></svg>Pre-fabricated cable looms</li>
      <li><svg viewBox="0 0 32 32" fill="none" stroke="#aaa" stroke-width="3"><circle cx="16" cy="16" r="5"/><path d="M16 3v6M16 23v6M3 16h6M23 16h6M7 7l4 4M21 21l4 4M25 7l-4 4M11 21l-4 4"/></svg>Fibre optic installation</li>
    </ul>
  </section>

  <section class="about">
    <h2 class="section-title"><em>ABOUT</em> <i>the company:</i></h2>
    <p>Velcor Lane provide cabling services for Broadcast Television and Audio Visual systems. With over 15 years experience working in these industries we can help with every aspect of design, project managment, installation and maintenance. Our projects range from fibre optic cabling at major sports events to installing and commisioning bespoke control systems on some of the worlds largest super yachts.</p>
  </section>

  <section class="other">
    <h2 class="section-title"><em>OTHER</em> <i>information:</i></h2>
    <p>The company is based in London, UK. Our projects often take place in other countries with work taking place accross Europe and beyond.</p>
    <p>We have a London based workshop for rack building and cable pre-fabrication.</p>
  </section>

  <svg class="footer-shape" viewBox="0 0 998 210" aria-hidden="true">
    <path d="M0 10H345q20 0 24 18l4 14q4 18 24 18H998V210H0Z" fill="#fff"/>
    <path d="M0 10H345q20 0 24 18l4 14q4 18 24 18H998" fill="none" stroke="var(--blue)" stroke-width="2"/>
    <path d="M395 62H998V150H395Z" fill="var(--blue-deep)"/>
    <rect x="0" y="150" width="998" height="60" fill="var(--dark)"/>
  </svg>

  <div class="brand">
    <span class="brand-dot"></span>
    <span class="brand-name">Velcor Lane</span>
  </div>

  <ul class="contact contact-a">
    <li class="phone"><svg viewBox="0 0 24 24" fill="var(--red)"><path d="M6 2l4 4-2 3a13 13 0 0 0 7 7l3-2 4 4-3 4C10 22 2 14 2 5z"/></svg>07700 900 418</li>
    <li><svg viewBox="0 0 24 24" fill="none" stroke="var(--red)" stroke-width="2"><rect x="2" y="5" width="20" height="14"/><path d="M2 5l10 8 10-8"/></svg>info@velcor-lane.com</li>
  </ul>
  <ul class="contact contact-b">
    <li><svg viewBox="0 0 24 24" fill="var(--red)"><path d="M12 2 1 12h3v10h6v-6h4v6h6V12h3z"/></svg>Address: TBC</li>
    <li><svg viewBox="0 0 24 24" fill="none" stroke="var(--red)" stroke-width="2"><circle cx="12" cy="12" r="10"/><path d="M2 12h20M12 2c4 4 4 16 0 20M12 2c-4 4-4 16 0 20"/></svg>www.velcor-lane.com</li>
  </ul>
</main>
</body>
</html>
```